Agriculture Business Card

I want to use my existing logo and use my tagline of "Don't Guess...Soil Test" on the card. Looking for a double sided card that will really get peoples attention.
Contact Info:
Marlow Field Crop Partners
Calvin Brusk
2716 K Lane
Brenfield, KS 66592
402-555-0143
calvin.r.brusk@fieldmailbox.net

```html
<!DOCTYPE html>
<html lang="en">
<head>
<meta charset="utf-8">
<title>Marlow Field Crop Partners – Business Card</title>
<link rel="stylesheet" href="https://fonts.googleapis.com/css2?family=Fira+Sans+Condensed:wght@500;600;700&display=swap">
<style>
  :root {
    --backdrop: #c2c3c5;
    --card: #ffffff;
    --green-dark: #24a645;
    --green-light: #52ba52;
    --soil: #a66a4e;
    --brand-brown: #9b5a3c;
    --gold: #f7b21b;
    --white: #ffffff;
  }
  * { box-sizing: border-box; margin: 0; padding: 0; }
  html, body {
    width: 900px; height: 1200px; overflow: hidden;
    background: var(--backdrop);
    font-family: "Fira Sans Condensed", "Arial Narrow", sans-serif;
  }
  .card {
    position: absolute;
    width: 657px; height: 375px;
    background: var(--card);
    border-radius: 12px;
    overflow: hidden;
  }
  .card--front { left: 123px; top: 190px; }
  .card--back  { left: 124px; top: 622px; }

  .brand-name {
    color: var(--brand-brown);
    font-weight: 600;
    text-align: center;
    line-height: 1.05;
    white-space: nowrap;
  }
  .card--front .brand-name {
    position: absolute; left: 0; right: 0; top: 236px;
    font-size: 28px;
  }
  .tagline-band {
    position: absolute; left: 0; right: 0; top: 321px; height: 30px;
    background: linear-gradient(90deg, var(--green-dark), var(--green-light));
    color: var(--white);
    font-weight: 600; font-size: 19px; letter-spacing: 1.6px;
    display: flex; align-items: center; justify-content: center;
  }

  .back-art { position: absolute; inset: 0; }
  .contact {
    position: absolute; left: 53px; top: 92px;
    color: var(--white);
  }
  .contact__name {
    color: var(--gold); font-weight: 700; font-size: 28px;
    letter-spacing: 0.5px; line-height: 1; text-transform: uppercase;
  }
  .contact__role { font-weight: 500; font-size: 15px; letter-spacing: 0.8px; margin-top: 4px; }
  .contact__rule { width: 105px; height: 1.5px; background: var(--gold); margin: 10px 0 8px; }
  .contact__line { font-weight: 500; font-size: 15px; letter-spacing: 0.9px; line-height: 26px; }
  .contact__item { display: flex; align-items: center; gap: 7px; }
  .contact__item svg { width: 13px; height: 13px; flex: none; }
  .card--back .brand-name {
    position: absolute; left: 414px; width: 200px; top: 228px;
    font-size: 24px;
  }
</style>
</head>
<body>
  <section class="card card--front">
    <p class="brand-name">Marlow Field Crop<br>Partners</p>
    <div class="tagline-band">DON'T GUESS...SOIL TEST</div>
  </section>

  <section class="card card--back">
    <svg class="back-art" viewBox="0 0 657 375" width="657" height="375" aria-hidden="true">
      <defs>
        <linearGradient id="fieldGreen" x1="0" y1="1" x2="1" y2="0">
          <stop offset="0" stop-color="#22a340"/>
          <stop offset="1" stop-color="#50b84f"/>
        </linearGradient>
      </defs>
      <polygon points="0,0 443,0 256,375 0,375" fill="url(#fieldGreen)"/>
      <polygon points="443,0 467,0 283,375 256,375" fill="var(--soil)"/>
      <line x1="443" y1="0" x2="256" y2="375" stroke="#fff" stroke-width="2.2"/>
    </svg>

    <div class="contact">
      <p class="contact__name">Calvin Brusk</p>
      <p class="contact__role">Owner</p>
      <div class="contact__rule"></div>
      <p class="contact__line">2716 K Lane</p>
      <p class="contact__line">Brenfield, KS 66592</p>
      <div class="contact__rule"></div>
      <p class="contact__line contact__item">
        <svg viewBox="0 0 24 24"><path fill="#f7b21b" d="M6.6 10.8a15.1 15.1 0 0 0 6.6 6.6l2.2-2.2c.3-.3.7-.4 1-.2 1.1.4 2.3.6 3.6.6.6 0 1 .4 1 1V20c0 .6-.4 1-1 1A17 17 0 0 1 3 4c0-.6.4-1 1-1h3.5c.6 0 1 .4 1 1 0 1.3.2 2.5.6 3.6.1.3 0 .7-.2 1z"/></svg>
        402-555-0143
      </p>
      <p class="contact__line contact__item">
        <svg viewBox="0 0 24 24"><path fill="#f7b21b" d="M2 5h20v14H2z"/><path d="M2 5l10 8 10-8" fill="none" stroke="#2eaa47" stroke-width="2"/></svg>
        calvin.r.brusk@fieldmailbox.net
      </p>
    </div>

    <p class="brand-name">Marlow Field Crop<br>Partners</p>
  </section>
</body>
</html>
```